Bravo Glazing

We need a website design for a company based in Texas that specializes in doors and and windows.
Bravo Glazing is a leading window manufacturer of aluminum and vinyl windows, both serving the replacement and new construction markets. Bravo Glazing Inc. was created over 25 years ago when two existing window manufacturers with excellent reputations in their fields - merged. Bravo Glazing offers a complete line conforming to the needs of residential and commercial window markets.
The final design should be something that communicates professionalism and features they're key value propositions.
Example websites we like:
http://layouts.pebblecraft.example/qx/purse/
http://layouts.pebblecraft.example/qx/splashzone/
http://layouts.pebblecraft.example/qx/refit2/
This design should format the existing content to be more visually organized, improve the fonts to clearer and more readable, and make it easier for users to find services.
Brand guide is attached
Website images can be found here: https://share.vaultdrop.example/7kRtQmZxLpWeYb
Target Market(s)
Windows
Number of Pages Required
1 page
Look and feel
Each slider illustrates characteristics of the customer's brand and the style your logo design should communicate.

```html
<!DOCTYPE html>
<html lang="en">
<head>
<meta charset="utf-8">
<title>Bravo Glazing</title>
<link href="https://fonts.googleapis.com/css2?family=Open+Sans:wght@400;600;700&family=Titillium+Web:wght@400;600;700&display=swap" rel="stylesheet">
<style>
:root{
  --teal:#1f7d7a;
  --teal-dark:#17605e;
  --crimson:#a1213f;
  --gold:#c9a22a;
  --ink:#2a2a2a;
  --dark:#1f1f1f;
  --grey:#6b6b6b;
  --light:#f4f4f4;
  --white:#ffffff;
}
*{margin:0;padding:0;box-sizing:border-box}
html,body{width:1200px;height:3804px;overflow:hidden}
body{font-family:'Open Sans',Arial,sans-serif;color:var(--ink);background:var(--white);font-size:13px;line-height:1.6}
h2,h3,.nav a,.btn{font-family:'Titillium Web',Arial,sans-serif}
.section-title{font-size:32px;font-weight:600;text-align:center;letter-spacing:1px;color:#333}
.btn{display:inline-block;background:var(--gold);color:var(--white);font-size:12px;font-weight:600;padding:8px 30px;border-radius:3px;letter-spacing:1px;text-decoration:none}

/* top bar */
.topbar{height:48px;background:var(--dark);display:flex;align-items:center;justify-content:space-between;padding:0 72px}
.nav{display:flex;height:48px}
.nav a{color:var(--white);font-size:12px;font-weight:600;text-decoration:none;padding:0 16px;line-height:48px}
.nav a.active{background:var(--gold)}
.contact-mini{display:flex;gap:28px;color:#ddd;font-size:12px}
.contact-mini span{display:flex;align-items:center;gap:6px}

/* hero */
.hero{height:452px;position:relative;background:linear-gradient(180deg,#e9ebec 0%,#cfd3d5 55%,#9ea3a6 100%);display:flex;flex-direction:column;align-items:center;justify-content:center}
.hero-photo{position:absolute;inset:0}
.hero-content{position:relative;text-align:center;width:720px}
.brand{font-family:'Titillium Web',Arial,sans-serif;font-weight:700;color:var(--crimson);display:inline-flex;align-items:center;gap:14px}
.brand .dot{width:22px;height:22px;border-radius:50%;background:var(--gold)}
.hero .brand{font-size:64px;line-height:1}
.hero-text{margin-top:22px;font-size:13px;color:#333;font-weight:600;background:rgba(255,255,255,.55);padding:8px 16px}

/* about */
.about{height:560px;display:flex;position:relative}
.about-left{width:520px;background:var(--teal)}
.about-right{flex:1;background:var(--crimson)}
.about-photo{position:absolute;left:72px;top:220px;width:516px;height:260px;background:linear-gradient(135deg,#8a4b2b,#c9a27a 45%,#6f8f5c);box-shadow:0 6px 16px rgba(0,0,0,.3)}
.about-copy{position:absolute;left:608px;top:46px;width:520px;color:var(--white)}
.about-copy h2{font-size:36px;font-weight:600;letter-spacing:1px;margin-bottom:12px}
.about-copy h2::after{content:"";display:block;width:40px;height:3px;background:var(--white);margin-top:4px}
.about-copy p{font-size:12.5px;line-height:1.75}
.about-copy .btn{margin-top:24px}

/* services */
.services{height:700px;padding-top:64px;background:var(--white)}
.service-grid{width:1056px;margin:46px auto 0;display:grid;grid-template-columns:1fr 1fr;column-gap:52px;row-gap:40px}
.service{display:flex;gap:20px}
.service-img{width:228px;height:200px;flex:none}
.service h3{font-size:20px;font-weight:600;color:#333;margin:6px 0 8px}
.service p{font-size:12.5px;color:var(--grey)}
.services .btn-wrap{text-align:center;margin-top:62px}

/* style */
.style{height:720px;background:linear-gradient(180deg,#3a3a3a,#1e1e1e);padding-top:62px}
.style .section-title{color:var(--white)}
.style-card{width:1056px;height:508px;margin:40px auto 0;background:var(--white);display:flex;gap:40px;padding:28px 28px}
.style-item{flex:1;text-align:center}
.style-img{height:270px}
.style-item h3{font-size:24px;font-weight:600;letter-spacing:1px;margin-top:24px;color:#333}
.style-item p{font-size:12.5px;color:var(--grey);width:420px;margin:6px auto 0}
.style-item .link{display:inline-block;margin-top:10px;font-size:12px;color:var(--crimson);font-weight:600;border-bottom:1px solid var(--crimson)}

/* testimonial */
.testimonial{height:420px;background:linear-gradient(180deg,#2a8b87,#1b6d6b);padding-top:56px;position:relative}
.testimonial .section-title{color:var(--white)}
.quote-box{position:absolute;left:72px;top:176px;width:1056px;height:180px}
.quote-frame{position:absolute;left:120px;top:0;right:0;bottom:0;border:2px solid var(--gold)}
.quote-photo{position:absolute;left:8px;top:0;width:180px;height:180px;border-radius:50%;background:linear-gradient(135deg,#e8e2d8,#b9a48c);border:5px solid var(--white)}
.quote-mark{position:absolute;left:150px;top:0;width:44px;height:44px;border-radius:50%;background:var(--crimson);color:var(--white);font-size:30px;font-family:Georgia,serif;text-align:center;line-height:50px}
.quote-text{position:absolute;left:240px;top:16px;width:780px;color:var(--white);font-size:13px;line-height:1.8}
.dots{position:absolute;left:0;right:0;top:384px;display:flex;justify-content:center;gap:8px}
.dots span{width:8px;height:8px;border-radius:50%;background:var(--gold)}

/* news */
.news{height:560px;padding-top:76px}
.news-grid{width:1056px;margin:40px auto 0;display:grid;grid-template-columns:repeat(4,1fr);gap:24px}
.news-img{height:180px}
.news-date{font-size:11px;color:var(--grey);margin-top:14px}
.news p{font-size:12.5px;color:#444;margin-top:4px}

/* footer */
.footer{height:364px;background:var(--dark);color:#ccc;position:relative}
.footer .brand{position:absolute;left:0;right:0;top:36px;justify-content:center;font-size:44px;color:var(--gold)}
.footer-cols{position:absolute;top:130px;left:72px;right:72px;display:flex}
.footer-col h4{font-family:'Titillium Web',Arial,sans-serif;font-size:16px;color:var(--white);font-weight:600;margin-bottom:12px}
.footer-col h4::after{content:"";display:block;width:30px;height:2px;background:var(--gold);margin-top:4px}
.footer-col.contact{width:476px}
.footer-col.links{width:300px}
.contact-line{display:flex;gap:10px;align-items:flex-start;font-size:12px;margin-bottom:8px}
.links a{display:block;color:#ccc;font-size:12px;text-decoration:none;margin-bottom:6px}
.social{display:flex;gap:8px;margin-bottom:12px}
.social span{width:24px;height:24px;background:#3b7cc4}
.copyright{font-size:11px}
</style>
</head>
<body>

<header class="topbar">
  <nav class="nav">
    <a class="active" href="#">HOME</a>
    <a href="#">ABOUT US</a>
    <a href="#">SERVICES</a>
    <a href="#">WORK</a>
    <a href="#">TESTIMONIAL</a>
    <a href="#">CONTACT US</a>
  </nav>
  <div class="contact-mini">
    <span><svg width="12" height="12" viewBox="0 0 24 24"><path fill="#c9a22a" d="M6.6 10.8a15 15 0 0 0 6.6 6.6l2.2-2.2a1 1 0 0 1 1-.25 11.4 11.4 0 0 0 3.6.57 1 1 0 0 1 1 1V20a1 1 0 0 1-1 1A17 17 0 0 1 3 4a1 1 0 0 1 1-1h3.5a1 1 0 0 1 1 1c0 1.25.2 2.45.57 3.6a1 1 0 0 1-.25 1z"/></svg>(512) 555-0148</span>
    <span><svg width="13" height="10" viewBox="0 0 26 20"><rect x="1" y="1" width="24" height="18" fill="none" stroke="#c9a22a" stroke-width="2"/><path d="M1 1l12 10L25 1" fill="none" stroke="#c9a22a" stroke-width="2"/></svg>info@bravoglazing.example</span>
  </div>
</header>

<section class="hero">
  <div class="hero-photo" role="img" aria-label="Bright white kitchen with large windows and stone backsplash"></div>
  <div class="hero-content">
    <div class="brand"><span class="dot"></span>Bravo Glazing</div>
    <p class="hero-text">Lorem Ipsum is simply dummy text of the printing and typesetting industry. Lorem Ipsum has been the industry's standard dummy text ever since the 1500s, when an unknown printer.</p>
  </div>
</section>

<section class="about">
  <div class="about-left"></div>
  <div class="about-right"></div>
  <div class="about-photo" role="img" aria-label="Wooden pergola over a patio in front of a house with glass doors"></div>
  <div class="about-copy">
    <h2>ABOUT US</h2>
    <p>Lorem Ipsum is simply dummy text of the printing and typesetting industry. Lorem Ipsum has been the industry's standard dummy text ever since the 1500s, when an unknown printer took a galley of type and scrambled it to make a type specimen book. It has survived not only five centuries, but also the leap into electronic typesetting, remaining essentially unchanged. It was popularised in the 1960s with the release of Letraset sheets containing Lorem Ipsum passages, and more recently with desktop publishing software like versions of Lorem Ipsum. Lorem Ipsum is simply dummy text of the printing and typesetting industry.</p>
    <a class="btn" href="#">READ MORE</a>
  </div>
</section>

<section class="services">
  <h2 class="section-title">WHAT WE DO</h2>
  <div class="service-grid">
    <div class="service">
      <div class="service-img" role="img" aria-label="House exterior with bay windows" style="background:linear-gradient(135deg,#6b5340,#b8a48f 60%,#e5e1da)"></div>
      <div><h3>Lorem Ipsum is simply</h3><p>Lorem Ipsum is simply dummy text of the printing and typesetting industry. Lorem Ipsum has been the industry's standard dummy text ever since the 1500s, when an unknown printer took a.</p></div>
    </div>
    <div class="service">
      <div class="service-img" role="img" aria-label="Modern white kitchen interior" style="background:linear-gradient(135deg,#f0eeea,#c9c2b6 60%,#7f6e5c)"></div>
      <div><h3>Lorem Ipsum is simply</h3><p>Lorem Ipsum is simply dummy text of the printing and typesetting industry. Lorem Ipsum has been the industry's standard dummy text ever since the 1500s, when an unknown printer took a.</p></div>
    </div>
    <div class="service">
      <div class="service-img" role="img" aria-label="Living room with wooden window frames" style="background:linear-gradient(135deg,#e4ddd2,#a88463 55%,#5a3f2b)"></div>
      <div><h3>Lorem Ipsum is simply</h3><p>Lorem Ipsum is simply dummy text of the printing and typesetting industry. Lorem Ipsum has been the industry's standard dummy text ever since the 1500s, when an unknown printer took a.</p></div>
    </div>
    <div class="service">
      <div class="service-img" role="img" aria-label="Sunroom with large windows overlooking a green garden" style="background:linear-gradient(135deg,#d9e2cf,#8aa86a 55%,#4b5c3a)"></div>
      <div><h3>Lorem Ipsum is simply</h3><p>Lorem Ipsum is simply dummy text of the printing and typesetting industry. Lorem Ipsum has been the industry's standard dummy text ever since the 1500s, when an unknown printer took a.</p></div>
    </div>
  </div>
  <div class="btn-wrap"><a class="btn" href="#">VIEW MORE</a></div>
</section>

<section class="style">
  <h2 class="section-title">CHOOSE YOUR STYLE</h2>
  <div class="style-card">
    <div class="style-item">
      <div class="style-img" role="img" aria-label="Residential kitchen with wooden cabinets and a window" style="background:linear-gradient(135deg,#b7542c,#e0b48a 50%,#f3ece2)"></div>
      <h3>RESIDENTIAL</h3>
      <p>Lorem Ipsum is simply dummy text of the printing and typesetting industry. Lorem Ipsum has been the industry's standard text.</p>
      <span class="link">VIEW ALL</span>
    </div>
    <div class="style-item">
      <div class="style-img" role="img" aria-label="Commercial space with wide glass windows and outdoor greenery" style="background:linear-gradient(135deg,#e8ebe6,#a7b59a 55%,#5f6a57)"></div>
      <h3>COMMERCIAL</h3>
      <p>Lorem Ipsum is simply dummy text of the printing and typesetting industry. Lorem Ipsum has been the industry's standard text.</p>
      <span class="link">VIEW ALL</span>
    </div>
  </div>
</section>

<section class="testimonial">
  <h2 class="section-title">TESTIMONIAL</h2>
  <div class="quote-box">
    <div class="quote-frame"></div>
    <div class="quote-photo" role="img" aria-label="Portrait of a smiling customer couple"></div>
    <div class="quote-mark">&ldquo;</div>
    <p class="quote-text">Lorem Ipsum is simply dummy text of the printing and typesetting industry. Lorem Ipsum has been the industry's standard dummy text ever since the 1500s, when an unknown printer took a galley of type and scrambled it to make a type specimen book. Lorem Ipsum is simply dummy text of the printing and typesetting industry. Lorem Ipsum has been the industry's standard dummy text ever since the 1500s, when an unknown printer took a galley.</p>
  </div>
  <div class="dots"><span></span><span></span><span></span></div>
</section>

<section class="news">
  <h2 class="section-title">NEWS</h2>
  <div class="news-grid">
    <article>
      <div class="news-img" role="img" aria-label="Modern grey house with large windows" style="background:linear-gradient(135deg,#8c959c,#c9cfd3 55%,#4c5258)"></div>
      <div class="news-date">MAY 8, 2017</div>
      <p>Lorem Ipsum is simply dummy text of the printing and typesetting industry.</p>
    </article>
    <article>
      <div class="news-img" role="img" aria-label="Bright kitchen with wooden cabinets" style="background:linear-gradient(135deg,#f1e7d3,#c89a5b 55%,#7b5430)"></div>
      <div class="news-date">MAY 8, 2017</div>
      <p>Lorem Ipsum is simply dummy text of the printing and typesetting industry.</p>
    </article>
    <article>
      <div class="news-img" role="img" aria-label="White kitchen interior with window" style="background:linear-gradient(135deg,#f4f4f2,#cfcac2 55%,#8d8579)"></div>
      <div class="news-date">MAY 8, 2017</div>
      <p>Lorem Ipsum is simply dummy text of the printing and typesetting industry.</p>
    </article>
    <article>
      <div class="news-img" role="img" aria-label="Warm wooden kitchen with window" style="background:linear-gradient(135deg,#a0582f,#deb98c 55%,#5c3a22)"></div>
      <div class="news-date">MAY 8, 2017</div>
      <p>Lorem Ipsum is simply dummy text of the printing and typesetting industry.</p>
    </article>
  </div>
</section>

<footer class="footer">
  <div class="brand">Bravo Glazing</div>
  <div class="footer-cols">
    <div class="footer-col contact">
      <h4>CONTACT US</h4>
      <div class="contact-line"><svg width="12" height="14" viewBox="0 0 24 28"><path fill="#ccc" d="M12 0a10 10 0 0 0-10 10c0 7.5 10 18 10 18s10-10.5 10-18A10 10 0 0 0 12 0zm0 14a4 4 0 1 1 0-8 4 4 0 0 1 0 8z"/></svg><span>Lorem Ipsum is simply dummy text of the<br>printing and typesetting industry.</span></div>
      <div class="contact-line"><svg width="12" height="12" viewBox="0 0 24 24"><path fill="#ccc" d="M6.6 10.8a15 15 0 0 0 6.6 6.6l2.2-2.2a1 1 0 0 1 1-.25 11.4 11.4 0 0 0 3.6.57 1 1 0 0 1 1 1V20a1 1 0 0 1-1 1A17 17 0 0 1 3 4a1 1 0 0 1 1-1h3.5a1 1 0 0 1 1 1c0 1.25.2 2.45.57 3.6a1 1 0 0 1-.25 1z"/></svg><span>(512) 555-0148</span></div>
      <div class="contact-line"><svg width="12" height="12" viewBox="0 0 24 24"><rect x="3" y="2" width="18" height="20" fill="none" stroke="#ccc" stroke-width="2"/></svg><span>(512) 555-0177</span></div>
      <div class="contact-line"><svg width="13" height="10" viewBox="0 0 26 20"><rect x="1" y="1" width="24" height="18" fill="none" stroke="#ccc" stroke-width="2"/><path d="M1 1l12 10L25 1" fill="none" stroke="#ccc" stroke-width="2"/></svg><span>info@bravoglazing.example</span></div>
    </div>
    <div class="footer-col links">
      <h4>QUICK LINKS</h4>
      <a href="#">HOME</a><a href="#">ABOUT US</a><a href="#">SERVICES</a><a href="#">WORK</a><a href="#">TESTIMONIAL</a><a href="#">CONTACT US</a>
    </div>
    <div class="footer-col follow">
      <h4>FOLLOW US</h4>
      <div class="social"><span></span><span></span><span></span><span></span><span></span></div>
      <p class="copyright">Copyright &copy; 2017 | All Rights Reserved</p>
    </div>
  </div>
</footer>

</body>
</html>
```